Brightmere Business Card Redesign & Logo Update

We need to update our business cards to something more modern and fresh. Brightmere can provide the current color schemes and old design examples, but welcome creativity in helping us with this redesign. PLEASE NOTE that we no longer utilize the "tree" and/or "leaf" imagery in our branding. If able would apprecaite an update on the quality of our "words only" logo in Ai. / PNG formats too.

Target Market(s)

Investors, landowners, corporate partners, contractors

Industry/Entity Type

Environmental Restoration & Conservation

Contact Information for Business Card

Logo, persons name, title, mailing address, phone and email, website url

Font styles to use
Other font styles liked:
• Merriweather

Requirements
Nice to have
• Logo, persons name, title, mailing address, phone and email, website url, but open to ideams
Should not have
• No all back backgrounds

```html
<!DOCTYPE html>
<html lang="en">
<head>
<meta charset="utf-8">
<title>Brightmere Business Card</title>
<link rel="stylesheet" href="https://fonts.googleapis.com/css2?family=Merriweather:wght@400;700;900&display=swap">
<style>
  :root {
    --bg: #8a8a8c;
    --card-white: #ffffff;
    --brand-green: #1a7f3c;
    --brand-orange: #ec8526;
    --ink: #222222;
    --photo-dark: #2b2823;
    --photo-mid: #4a4238;
    --photo-light: #8d8a84;
  }
  * { margin: 0; padding: 0; box-sizing: border-box; }
  html, body { width: 900px; height: 1200px; overflow: hidden; }
  body { background: var(--bg); position: relative; font-family: "Merriweather", serif; }

  .card {
    position: absolute;
    left: 121px;
    width: 658px;
    height: 375px;
    border-radius: 14px;
    overflow: hidden;
  }
  .card--front { top: 204px; }
  .card--back { top: 621px; background: var(--card-white); }

  .front-photo {
    position: absolute; inset: 0;
    background:
      radial-gradient(ellipse 22% 70% at 48% 45%, rgba(141,138,132,0.55), transparent 70%),
      linear-gradient(135deg, var(--photo-mid), var(--photo-dark) 55%, var(--photo-mid));
  }
  .front-logo {
    position: absolute; left: 0; right: 0; top: 134px;
    text-align: center;
  }
  .brand-name {
    font-family: "Merriweather", serif;
    font-weight: 900;
    color: var(--brand-green);
    letter-spacing: 0.5px;
    line-height: 1;
  }
  .front-logo .brand-name { font-size: 52px; }
  .brand-tagline {
    font-family: "Merriweather", serif;
    font-weight: 400;
    line-height: 1;
  }
  .front-logo .brand-tagline { color: #ffffff; font-size: 20px; margin-top: 18px; letter-spacing: 0.5px; }

  .back-logo {
    position: absolute; left: 40px; width: 272px; top: 150px;
    text-align: center;
  }
  .back-logo .brand-name { font-size: 33px; }
  .back-logo .brand-tagline { color: var(--ink); font-size: 14px; margin-top: 10px; }

  .divider {
    position: absolute; left: 328px; top: 100px;
    width: 2px; height: 175px; background: var(--ink);
  }

  .contact { position: absolute; left: 354px; top: 96px; color: var(--ink); }
  .contact__name { font-size: 25px; font-weight: 700; line-height: 1; }
  .contact__first { color: var(--brand-orange); }
  .contact__last { color: var(--brand-green); }
  .contact__title { font-size: 16px; margin-top: 8px; }
  .contact__address { font-size: 16px; line-height: 24px; margin-top: 10px; }
  .contact__lines { list-style: none; margin-top: 6px; font-size: 16px; line-height: 24px; letter-spacing: 0.4px; }
  .contact__lines li { display: flex; align-items: center; gap: 7px; }
  .contact__lines svg { width: 13px; height: 13px; fill: var(--brand-orange); flex: none; }

  .social { position: absolute; left: 0; right: 0; top: 312px; display: flex; justify-content: center; gap: 13px; }
  .social__dot { width: 32px; height: 32px; border-radius: 50%; }
  .social__dot--green { background: var(--brand-green); }
  .social__dot--orange { background: var(--brand-orange); }
</style>
</head>
<body>
  <section class="card card--front">
    <div class="front-photo" role="img" aria-label="Photograph of a woodland stream cascading over mossy rocks with fallen autumn leaves, darkened"></div>
    <div class="front-logo">
      <div class="brand-name">BRIGHTMERE</div>
      <div class="brand-tagline">Land Restoration Partners</div>
    </div>
  </section>

  <section class="card card--back">
    <div class="back-logo">
      <div class="brand-name">BRIGHTMERE</div>
      <div class="brand-tagline">Land Restoration Partners</div>
    </div>
    <div class="divider"></div>
    <div class="contact">
      <div class="contact__name"><span class="contact__first">ALEX</span> <span class="contact__last">MORGAN</span></div>
      <div class="contact__title">Director</div>
      <div class="contact__address">4820 Meadow Lane 17,<br>Avalon, TX 75010</div>
      <ul class="contact__lines">
        <li><svg viewBox="0 0 24 24"><path d="M6.6 10.8a15.2 15.2 0 0 0 6.6 6.6l2.2-2.2a1 1 0 0 1 1-.25 11.4 11.4 0 0 0 3.6.57 1 1 0 0 1 1 1V20a1 1 0 0 1-1 1A17 17 0 0 1 3 4a1 1 0 0 1 1-1h3.5a1 1 0 0 1 1 1c0 1.25.2 2.45.57 3.57a1 1 0 0 1-.25 1z"/></svg>(555) 014-2287</li>
        <li><svg viewBox="0 0 24 24"><path d="M2 5h20v2l-10 6L2 7z"/><path d="M2 9l10 6 10-6v10H2z"/></svg>info@brightmerecredits.com</li>
        <li><svg viewBox="0 0 24 24"><path d="M12 2a10 10 0 1 0 0 20 10 10 0 0 0 0-20zm6.9 6h-2.9a15 15 0 0 0-1.4-3.6A8 8 0 0 1 18.9 8zM12 4a13 13 0 0 1 1.9 4h-3.8A13 13 0 0 1 12 4zM4.3 14a8 8 0 0 1 0-4h3.4a16 16 0 0 0 0 4zm.8 2h2.9a15 15 0 0 0 1.4 3.6A8 8 0 0 1 5.1 16zM8 8H5.1a8 8 0 0 1 4.3-3.6A15 15 0 0 0 8 8zm4 12a13 13 0 0 1-1.9-4h3.8A13 13 0 0 1 12 20zm2.3-6H9.7a14 14 0 0 1 0-4h4.6a14 14 0 0 1 0 4zm.3 5.6a15 15 0 0 0 1.4-3.6h2.9a8 8 0 0 1-4.3 3.6zm1.7-5.6a16 16 0 0 0 0-4h3.4a8 8 0 0 1 0 4z"/></svg>www.brightmerecredits.com</li>
      </ul>
    </div>
    <div class="social" aria-label="Social profiles">
      <span class="social__dot social__dot--green"></span>
      <span class="social__dot social__dot--orange"></span>
      <span class="social__dot social__dot--green"></span>
    </div>
  </section>
</body>
</html>
```